依頼詳細
店舗かんばんのデザインをお願いしたく思います。ただし、仕様がタペストリーとなります。(壁に貼り付ける感じです)
重視したい事は、第一目立つこと。文字のなかではお葬式相談室の文字を一番目立たしたいです。店内の雰囲気はちょっとしたカフェのような感じなので、入りやすいような、やわらかいイメージのデザインが好ましいです。また、お葬式自体暗いイメージなので明るい印象もつけたいです。
記載項目
お葬式相談室/桐野葬祭/電話番号/ルミナード楓/いろんなありがとうがあるお葬式を・・・。
参考:http://www.kanade-hall.co.jp/
希望イメージ
シンプル 複雑
単色 カラフル
暗い 明るい
日常 高級
遊び心 厳粛
未来的 伝統的
女性的 男性的
希望する色
納品ファイル
• 高解像度JPG (.jpg)
• イラストレーター形式 (.ai)
補足説明
納品ファイルは、後日ご連絡致します。また、会社のロゴデータも後日添付致します
サイズ:W1800 H2800となります。
皆様。お世話になります。
たくさんのご提案ありがとうございます。

追記内容についてですが、2点ございます。
①「お葬式相談室」の上部、キャッチの部分に「お葬式のご相談・お悩みが解決できる」と記載して頂きたいと思います。
②「お葬式相談室」下記部分には「仏壇・ろうそく・線香も取り扱っております」と記載して頂きたいと思います。
※ただ、こちらについて仏壇を取り扱うかどうか、まだ確定していない事もあり、場合によっては、「仏壇」の部分を「仏花」に変えて頂く場合もございます。

今回、修正がございましたので、締切期間を延期させて頂きます。

みなさまには、ご迷惑をおかけいたしますが、
何卒、よろしくお願い申し上げます。
皆様。お世話になります。下記追記内容を記載します。

①弊社では、コーポレートカラーを青としており、他の店舗看板など販促物も青と白を基調にしている事が多いので、今回も同じように合わす事ができればと思います。

②ロゴはコスモスを表しております。
背景にコスモスの花を入れて頂いたりするデザインがあれば一度拝見してみたいと考えております。また、ご家族の写真を記載したデザインも安心感が訴求されるので、
一度見てみたいと思います。

③道を挟んだ場所に区役所がございます。看板を見られるメインの対象者となります。なので、その距離感を踏まえ、文字等の大きさの調整を行って頂ければと思います。下記は、看板の構成を記載しております。

【フック(左上)どんなお店か】「お葬式の相談・お悩み事が解決できる」⇒【タイトル】「お葬式相談室」⇒【なにを扱っているか】「仏壇・ろうそく・線香(大きく)」取り扱っております。⇒【どの会社が】「いろんなありがとうがあるお葬式を・・・桐野葬祭」(ルミナード楓より桐野葬祭の方が大きめでお願いします。)
⇒【問い合わせ】TEL(24時間~)

参考までに、現在の店舗写真を添付致します。撮影場所は上記でご説明させて頂いた、区役所前からの写真となります。

何卒、宜しくお願い致します。
看板設置イメージを添付致します。

P.S
一度会議で、デザインを相談したいと考えているためできれば30日までにご連絡いただけると幸いです。

宜しくお願い致します。
■ 選んだ理由

お世話になります。今回、この提案を選んだ理由は、こちらの希望に沿い、弊社の”らしさ”を忠実の表現して頂いたからです。
また、目立たせるポイントの色使いなども気に入りました。

■ 提案者全員のお礼・コメント

今回、提案していただいたみなさまへ。
はじめての利用という事もあり、みなさまへのご配慮が足りない部分もありましたが、たくさんのご提案ありがとうございました。

また、機会があればどうぞ宜しくお願い致します。

```html
<!DOCTYPE html>
<html lang="ja">
<head>
<meta charset="utf-8">
<title>桐野葬祭 お葬式相談室</title>
<link rel="stylesheet" href="https://fonts.googleapis.com/css2?family=M+PLUS+Rounded+1c:wght@500;700;800;900&display=swap">
<style>
  :root {
    --leaf-light: #e9f6c8;
    --leaf-mid: #a9d55a;
    --leaf-deep: #5da12c;
    --ink-green: #1f5a1c;
    --banner-green: #2f7d2a;
    --title-yellow: #ffe600;
    --title-edge: #3d3a12;
    --accent-pink: #e8307a;
    --phone-red: #e2262e;
    --icon-grey: #555555;
    --white: #ffffff;
  }
  * { margin: 0; padding: 0; box-sizing: border-box; }
  html, body { width: 787px; height: 1200px; overflow: hidden; background: var(--white); }
  body { font-family: "M PLUS Rounded 1c", sans-serif; }

  .tapestry { position: relative; width: 787px; height: 1200px; overflow: hidden; }

  .leaf-backdrop {
    position: absolute; inset: 0;
    background:
      radial-gradient(ellipse at 50% 45%, var(--leaf-light) 0%, rgba(233,246,200,0.6) 35%, transparent 70%),
      radial-gradient(ellipse at 0% 100%, var(--leaf-deep) 0%, transparent 55%),
      radial-gradient(ellipse at 100% 90%, var(--leaf-deep) 0%, transparent 50%),
      radial-gradient(ellipse at 100% 15%, var(--leaf-mid) 0%, transparent 45%),
      linear-gradient(180deg, var(--leaf-mid) 0%, #c6e58a 50%, var(--leaf-mid) 100%);
  }

  .top-band {
    position: absolute; left: 0; top: 0; width: 100%; height: 70px;
    background: linear-gradient(180deg, var(--white) 0%, rgba(255,255,255,0.85) 70%, rgba(255,255,255,0) 100%);
  }
  .brand-mark {
    position: absolute; left: 62px; top: 12px; width: 40px; height: 40px;
    border-radius: 50%; background: var(--banner-green);
  }
  .company-banner {
    position: absolute; left: 228px; top: 10px; width: 220px; height: 50px;
    background: var(--banner-green); border-radius: 6px;
    color: var(--white); font-weight: 800; font-size: 38px; line-height: 50px;
    text-align: center; letter-spacing: 2px;
  }
  .years-badge {
    position: absolute; left: 456px; top: 12px; width: 84px; height: 46px;
    background: var(--white); border: 3px solid var(--banner-green); border-radius: 6px;
    color: var(--banner-green); font-weight: 800; font-size: 15px; line-height: 1.1;
    display: flex; align-items: center; justify-content: center; text-align: center;
  }
  .years-badge b { font-size: 24px; }

  .outlined {
    -webkit-text-stroke: 8px var(--white);
    paint-order: stroke fill;
  }

  .catch {
    position: absolute; left: 0; top: 168px; width: 100%;
    text-align: center; color: var(--ink-green);
    font-weight: 900; font-size: 44px; line-height: 52px; letter-spacing: 1px;
  }
  .catch em { font-style: normal; color: var(--accent-pink); }

  .title {
    position: absolute; left: 0; top: 380px; width: 100%;
    text-align: center; color: var(--title-yellow);
    font-weight: 900; font-size: 170px; line-height: 152px; letter-spacing: 2px;
    -webkit-text-stroke: 12px var(--title-edge);
    paint-order: stroke fill;
    text-shadow: 0 0 18px rgba(255,255,255,0.9);
  }

  .freecall {
    position: absolute; left: 192px; top: 806px;
    display: flex; align-items: center; gap: 16px;
  }
  .freecall-square {
    width: 56px; height: 56px; border-radius: 6px;
    background: var(--white); border: 4px solid var(--icon-grey);
  }
  .freecall-label {
    color: var(--accent-pink); font-weight: 700; font-size: 58px; line-height: 66px; letter-spacing: 4px;
  }
  .phone {
    position: absolute; left: 0; top: 874px; width: 100%;
    text-align: center; color: var(--phone-red);
    font-weight: 700; font-size: 84px; line-height: 96px; letter-spacing: 2px;
  }
  .mobile-note {
    position: absolute; left: 0; top: 978px; width: 100%;
    text-align: center; color: var(--phone-red);
    font-weight: 900; font-size: 36px; line-height: 46px;
  }

  .hall {
    position: absolute; left: 150px; top: 1036px;
    display: flex; align-items: center; gap: 30px;
  }
  .hall-dot { width: 80px; height: 80px; border-radius: 50%; background: var(--banner-green); }
  .hall-name {
    color: var(--ink-green); font-weight: 800; font-size: 58px; letter-spacing: 3px;
  }
</style>
</head>
<body>
<main class="tapestry">
  <div class="leaf-backdrop" role="img" aria-label="明るい緑の葉と小さな白い花の背景"></div>
  <div class="top-band"></div>

  <div class="brand-mark"></div>
  <div class="company-banner">桐野葬祭</div>
  <div class="years-badge"><span>創業<b>70</b>余年</span></div>

  <p class="catch outlined">
    いろんな<em>ありがとう</em>がある<br>
    お葬式を安心料金で<br>
    ご提供させて頂きます。
  </p>

  <h1 class="title">お葬式<br>相談室</h1>

  <div class="freecall">
    <span class="freecall-square"></span>
    <span class="freecall-label outlined">フリーコール</span>
  </div>
  <p class="phone outlined">0120-38-5172</p>
  <p class="mobile-note outlined">携帯・スマホからもお電話OK！</p>

  <div class="hall">
    <span class="hall-dot"></span>
    <span class="hall-name outlined">ルミナード楓</span>
  </div>
</main>
</body>
</html>
```